Brightmoor Learning Brochure Design Project

Our company requires a brochure for promoting our Corporate Training business.

Please use data from Corporate training brochure doc.
Updates

Dear Designers,

We have added new corporate brochure document into the project. Use this data to finish up your brochure.

Thanks,

Omar Kasprzak

Reason: We have recently finalised the data that will go into the corporate brochure.

Reason: To get more better designs

Target Market(s)

Training Managers / Business Managers / Hiring Managers

Industry/Entity Type

Training

Requirements
Must have
• Corporate and Professional Look

```html
<!DOCTYPE html>
<html lang="en">
<head>
<meta charset="utf-8">
<title>Brightmoor Learning – Corporate Training Brochure</title>
<link href="https://fonts.googleapis.com/css2?family=Arimo:wght@400;700&display=swap" rel="stylesheet">
<style>
  :root {
    --paper: #ffffff;
    --ink: #2b2b2b;
    --heading: #1f1f1f;
    --sky: #a9c8dc;
    --mist: #e3e4e5;
    --photo-office-a: #5a4a42;
    --photo-office-b: #c9b8a8;
    --photo-lobby-a: #3d4a4c;
    --photo-lobby-b: #8a8f88;
  }
  * { margin: 0; padding: 0; box-sizing: border-box; }
  html, body { width: 1200px; height: 849px; overflow: hidden; background: var(--paper); }
  .spread {
    position: relative; width: 1200px; height: 849px; overflow: hidden;
    font-family: "Arimo", Arial, sans-serif; color: var(--ink);
  }
  .spread__art { position: absolute; inset: 0; }
  .copy { position: absolute; font-size: 9.2px; line-height: 17px; }
  .copy h2 { font-size: 12.5px; font-weight: 400; color: var(--heading); margin-bottom: 15px; }
  .copy p { margin-bottom: 17px; }
  .copy--company { left: 36px; top: 97px; width: 370px; }
  .copy--training { left: 36px; top: 244px; width: 330px; }
  .copy--training h2 { margin-bottom: 20px; }
  .copy--training p { margin-bottom: 10px; }
  .benefits { list-style: none; }
  .benefits li { position: relative; padding-left: 22px; }
  .benefits li::before { content: "•"; position: absolute; left: 0; }
  .copy--testing { left: 637px; top: 362px; width: 350px; }
  .copy--testing h2 { margin-bottom: 22px; }
  .copy--testing p { margin-bottom: 19px; }
</style>
</head>
<body>
<main class="spread">
  <svg class="spread__art" width="1200" height="849" viewBox="0 0 1200 849" aria-hidden="false">
    <defs>
      <linearGradient id="office-tones" x1="0" y1="0" x2="1" y2="1">
        <stop offset="0" stop-color="var(--photo-office-a)"/>
        <stop offset="1" stop-color="var(--photo-office-b)"/>
      </linearGradient>
      <linearGradient id="lobby-tones" x1="0" y1="0" x2="1" y2="1">
        <stop offset="0" stop-color="var(--photo-lobby-b)"/>
        <stop offset="1" stop-color="var(--photo-lobby-a)"/>
      </linearGradient>
    </defs>
    <polygon class="facet facet--sky" points="150,0 815,0 430,132" fill="var(--sky)"/>
    <polygon class="facet facet--mist" points="430,132 940,0 815,0" fill="var(--mist)"/>
    <polygon class="facet facet--mist" points="430,132 940,0 600,195" fill="var(--mist)"/>
    <polygon class="facet facet--sky" points="600,195 690,222 600,288" fill="var(--sky)"/>
    <polygon class="photo photo--meeting" role="img" aria-label="Photo: trainees seated around a desk in a meeting with an instructor"
      points="940,0 1200,0 1200,398 690,222" fill="url(#office-tones)"/>
    <polygon class="photo photo--lobby" role="img" aria-label="Photo: a professional woman sitting on a wooden bench in a modern lobby"
      points="600,288 600,849 160,849 112,700" fill="url(#lobby-tones)"/>
    <polygon class="facet facet--mist" points="0,690 112,700 160,849 0,849" fill="var(--mist)"/>
  </svg>

  <section class="copy copy--company">
    <h2>Our Company</h2>
    <p>Incepted in the year 1992, Brightmoor Learning Ltd. (Corvane Gold Partner, Altrix WDP Partner, Nexora CENS Partner) is India’s leading ISO certified I.T. education provider. Known as a “one stop, training shop”, Brightmoor is a pioneer in high-end I.T. (Networking, Software, Security and Cloud Computing), Soft Skills and Leadership Training. With operations in India, Africa, South East Asia and the Middle East, Brightmoor manages to seamlessly provide training to satisfy local needs.</p>
  </section>

  <section class="copy copy--training">
    <h2>Our Training</h2>
    <p>Brightmoor believes in offering the finest standards of training that is constantly updated and adapted to the changing global scenario. Our training is geared towards ‘increasing employability’.</p>
    <ul class="benefits">
      <li>All trainers are certified by partner technology company – be it Nexora, Corvane, Certivo or Altrix</li>
      <li>All courses are developed with input and approval from companies in the I.T., Banking, Telecom and Manufacturing industries</li>
      <li>Emphasis on bridging the ‘industry-academia’ gap. Therefore there is a keen focus on industry related projects thus developing a directly employable workforce</li>
      <li>An arrangement of credit transfer with Ashgrove University UK and affiliation with Government institutions like National Open Learning University (NOLU), Hillcrest Valley University (HVU), TECHBOARD and more, ensures that the curriculum, education system and training methodologies are at par with the international standards.</li>
    </ul>
  </section>

  <section class="copy copy--testing">
    <h2>Testing And Certifications</h2>
    <p>Brightmoor Learning Limited is a leading provider of Testing &amp; Certification Services in India. We have regularly serviced the Testing &amp; certification requirements of students and professionals from various corporates, by providing a consistently satisfactory performance with all the relevant facilities.</p>
    <p>One of the largest Gold Partners of Corvane, Altrix, CENS (Career Education in Nexora Software) and is a leading testing and certification site for Testwell and Examtrack. Brightmoor is also a Leading Certified Partners for Learning Solutions (CPLS) for Corvane Suite ERP and CRM 4.0.</p>
    <p>We strongly believe in the power of Word-of-Mouth for business growth. This has installed in us the drive to take every initiative to provide the best of services to every customer eachtime. This has transformed us into a highly reputed, respected &amp; preferred destination for all kinds of Testing &amp; Certification requirements across various industries.</p>
  </section>
</main>
</body>
</html>
```